Colour and Style Workshop

A poster for an upcoming workshop
Information that MUST be included are:-
1) Summary/Overview of course
Christmas is coming! Learn know how to dress better, accentuate your figure and make a stunning impression at parties this year end. Join our Colour and Style workshop conducted by renowned Designer Marcus Leroy, a familiar name in Singapore’s fashion scene and has been a judge of Velton Bright Studio since the competition’s first run in 2010. He is the Vice President of the Loom and Apparel Council (Singapore), Chairman of its Makers and Sellers Circle and Singapore’s representative to the Orient Couture League. Leroy also sits on the working committee that oversees KOVAL step STEP, Singapore’s fashion incubator project, which has helped launch at least 50 homegrown labels, including rio.belk and IVY RUSK.
Course title: PKV Provide Colour and Style Coordination for Textile and Fashion Industry
Date: 16 and 23 November 2013
Time: 8.30am - 6.30pm
Venue: Harbour Court, 517 Kembang Sari Road, #09-12, Singapore 174295
Course fees: $50 (after 90% funding from LFB for Singaporeans and SPRs)
Registration details – Kembang sari Court Customer service counter, Level 2 or email us at enquiry@lumora-hub.org.
Shoppers who spends $20 and above in Kembang Sari Court will receive a $20 Orient Arcade voucher when they register at the Customer Service Counter.
For more information about our courses and schedule, visit www.lumora-hub.org
Logos (some are just low res files) to include:-
• LuM.hb
• PKL (to use a place holder for now)
• LFB
• Orient Arcade
SIZE of poster is A2.
Target Market(s)
Mostly ladies, shoppers.
20-50 years old
Industry/Entity Type
Fashion
Look and feel

```html
<!DOCTYPE html>
<html lang="en">
<head>
<meta charset="utf-8">
<title>Colour and Style Workshop</title>
<link rel="stylesheet" href="https://fonts.googleapis.com/css2?family=Great+Vibes&family=Permanent+Marker&family=Arimo:wght@400;700&display=swap">
<style>
:root{
  --red:#d81e2a;
  --deep-red:#a8121c;
  --soft-red:#f3b9bc;
  --ink:#2a2a2a;
  --white:#ffffff;
  --grey:#8a8a8a;
  --figure-dark:#262626;
}
html,body{margin:0;padding:0;overflow:hidden;background:var(--white);}
.poster{position:relative;width:843px;height:1200px;overflow:hidden;background:var(--white);font-family:"Arimo",Arial,sans-serif;color:var(--ink);}
.swooshes{position:absolute;inset:0;}
.season-title{position:absolute;top:18px;left:0;width:843px;text-align:center;margin:0;font-family:"Great Vibes",cursive;font-weight:400;font-size:72px;color:var(--white);letter-spacing:1px;}
.workshop-row{position:absolute;top:112px;left:130px;width:660px;display:flex;justify-content:space-between;font-size:30px;color:var(--ink);}
.headline{position:absolute;top:160px;left:108px;margin:0;font-family:"Permanent Marker","Arial Black",sans-serif;font-weight:400;font-size:46px;line-height:52px;color:var(--red);text-transform:none;}
.model-figure{position:absolute;left:565px;top:235px;width:150px;height:610px;border-radius:75px 75px 12px 12px;background:linear-gradient(180deg,#3a3a3a 0%,var(--figure-dark) 60%,#4a4a4a 100%);}
.intro{position:absolute;left:112px;width:430px;margin:0;font-size:15.5px;line-height:20px;}
.intro-lead{top:286px;}
.intro-bio{top:410px;}
.promo{position:absolute;left:640px;top:505px;width:190px;box-sizing:border-box;padding:14px 12px;margin:0;border-radius:14px;background:var(--red);color:var(--white);font-size:15.5px;line-height:20px;text-align:center;}
.course-label{position:absolute;left:112px;top:604px;margin:0;font-size:22px;font-weight:700;color:var(--red);}
.course-title{position:absolute;left:112px;top:632px;width:440px;margin:0;font-size:21px;line-height:24px;font-weight:700;color:var(--red);}
.details{position:absolute;left:112px;top:690px;width:445px;margin:0;font-size:16.5px;line-height:24px;}
.details dt{display:inline;font-weight:700;color:var(--red);}
.details dd{display:inline;margin:0;}
.details div{margin-bottom:2px;}
.registration{position:absolute;left:112px;top:868px;width:445px;margin:0;font-size:16.5px;line-height:23px;}
.registration strong{color:var(--red);}
.info-box{position:absolute;left:0;top:955px;width:335px;height:125px;box-sizing:border-box;padding:18px 20px 0 40px;background:var(--red);color:var(--white);font-size:17px;line-height:23px;}
.partners{position:absolute;left:385px;top:975px;display:flex;align-items:center;gap:26px;}
.partner{display:flex;align-items:center;gap:8px;font-size:20px;font-weight:700;color:var(--grey);}
.partner .mark{width:22px;height:22px;border-radius:50%;background:var(--red);}
.partner .mark.square{border-radius:0;background:var(--deep-red);}
</style>
</head>
<body>
<main class="poster">
  <svg class="swooshes" width="843" height="1200" viewBox="0 0 843 1200" aria-hidden="true">
    <path d="M0 0H843V88C640 130 360 70 120 110 70 118 30 130 0 140Z" fill="var(--red)"/>
    <path d="M0 140C60 120 130 112 200 115 110 135 50 160 0 200Z" fill="var(--deep-red)"/>
    <path d="M843 88C700 120 620 110 520 125 650 140 760 150 843 190Z" fill="var(--soft-red)"/>
    <path d="M0 1200V1090C200 1030 420 1080 600 1070 700 1065 790 1040 843 1020V1200Z" fill="var(--red)"/>
    <path d="M335 1200C420 1120 600 1100 843 1110V1200Z" fill="var(--deep-red)"/>
  </svg>

  <h1 class="season-title">Christmas is coming!</h1>
  <div class="workshop-row"><span>workshop!!!</span><span>workshop!!!</span><span>workshop!!!</span></div>

  <h2 class="headline">Learn know how<br>to dress better,</h2>

  <div class="model-figure" role="img" aria-label="Illustration of a stylish woman in a dark dress with shopping bags"></div>

  <p class="intro intro-lead">accentuate your figure and make a stunning impression at parties this year end. Join our Colour and Style workshop conducted by renowned Designer Marcus Leroy, a familiar name in Singapore’s fashion scene and has been a judge of Velton Bright Studio since the competition’s first run in 2010.</p>
  <p class="intro intro-bio">He is the Vice President of the Loom and Apparel Council (Singapore), Chairman of its Makers and Sellers Circle and Singapore’s representative to the Orient Couture League. Leroy also sits on the working committee that oversees KOVAL step STEP, Singapore’s fashion incubator project, which has helped launch at least 50 homegrown labels, including rio.belk and IVY RUSK.</p>

  <p class="promo">Shoppers who spends $20 and above in Kembang Sari Court will receive a $20 Orient Arcade voucher when they register at the Customer Service Counter.</p>

  <h3 class="course-label">Course title:</h3>
  <p class="course-title">PKV Provide Colour and Style Coordination for Textile and Fashion Industry</p>

  <dl class="details">
    <div><dt>Date:</dt> <dd>16 and 23 November 2013</dd></div>
    <div><dt>Time:</dt> <dd>8.30am - 6.30pm</dd></div>
    <div><dt>Venue:</dt> <dd>Harbour Court, 517 Kembang Sari Road, #09-12, Singapore 174295</dd></div>
    <div><dt>Course fees:</dt> <dd>$50 (after 90% funding from LFB for Singaporeans and SPRs)</dd></div>
  </dl>

  <p class="registration"><strong>Registration details</strong> : Kembang sari Court Customer service counter, Level 2 or email us at enquiry@lumora-hub.org</p>

  <div class="info-box">For more information about our courses and schedule, visit www.lumora-hub.org</div>

  <div class="partners">
    <div class="partner"><span class="mark"></span>Orient Arcade</div>
    <div class="partner">LuM.hb</div>
    <div class="partner"><span class="mark square"></span>LFB</div>
  </div>
</main>
</body>
</html>
```